Epoxy Flooring Contractor business card

We need a business card to promote a new addition to our business. We now offer Epoxy Flooring. We would like for the business card to include the images attached. One is our logo, the other is a sample of metallic epoxy flooring, we would like to incorporate that somewhere into the design. I was thinking an icon of a man pushing a concrete grinder and have the color set to the metallic epoxy color. I found a business card sample on this website, I will attach it. It has the icon that we are looking for, or something similar.
Our company name is Harborline Coatings LLC
Our owners name is Dane Morrow
Phone is 561-482-7160
website is www.harborline-coatingsllc.example
please let me know if you need any other info

Contact Information for Business Card

Harborline Coatings LLC
Dane Morrow, owner
Phone: 561-482-7160
Address: P.O Box 8241 Lake Worth, FL 33467
www.Harborline-CoatingsLLC.example
HarborlineCoatingsLLC@mailbox.example
Include logo attached
It must include a Clip art of man with concrete grinder
Must include metallic epoxy design attached
Must include the following text
Residential Garage Flooring
Epoxy Countertops
Commercial Epoxy Flooring
Restaurant Flooring
Warehouse Flooring
Licensed & Insured
Free Estimates

Colors

Designer to choose colors to be used in the design.

Requirements
Must have
• Include logo attached
• It must include a Clip art of man with concrete grinder
• Must include metallic epoxy design attached
• Must include the following text
• Garage Epoxy Flooring
• Residential Epoxy Flooring
• Concrete Floor Crack Repairs
• Concrete Floor Grinding
• Commercial & Warehouse Epoxy Flooring
• Restaurant Epoxy Flooring
• Epoxy Countertops
• Non Slip Epoxy Pool Decks
• Textured Finishes, Flakes, Granite Coat, Metallic & Quartz
• FREE ESTIMATES • LICENSED & INSURED

```html
<!DOCTYPE html>
<html lang="en">
<head>
<meta charset="utf-8">
<title>Harborline Coatings – Business Card</title>
<link href="https://fonts.googleapis.com/css2?family=Montserrat:wght@400;500;700&family=Saira+Semi+Condensed:wght@500;600;700&display=swap" rel="stylesheet">
<style>
  :root{
    --bg:#e9ecf0;
    --paper:#ffffff;
    --ink:#5f6368;
    --ink-dark:#3f4246;
    --brand:#2f5f95;
    --brand-light:#6f9fd3;
    --epoxy-deep:#1f4f96;
    --epoxy-mid:#3c6fb8;
    --epoxy-light:#7ea3d6;
    --on-epoxy:#ffffff;
  }
  *{box-sizing:border-box;margin:0;padding:0}
  html,body{width:1200px;height:900px;overflow:hidden;background:var(--bg)}
  .canvas{position:relative;width:1200px;height:900px}
  .card{position:absolute;left:280px;width:640px;height:366px;overflow:hidden;box-shadow:0 8px 24px rgba(0,0,0,.18)}
  /* Front */
  .card--front{top:50px;background:var(--paper);font-family:"Montserrat",sans-serif}
  .front__rule-top{position:absolute;left:0;top:54px;width:210px;height:1.5px;background:var(--brand)}
  .front__logo{position:absolute;left:50px;top:120px;width:200px;display:flex;align-items:center;gap:10px}
  .front__logo-mark{width:18px;height:18px;background:var(--brand-light);flex:none}
  .front__logo-name{font-weight:700;font-size:21px;line-height:1.1;color:var(--ink-dark)}
  .front__divider{position:absolute;left:270px;top:92px;width:1.5px;height:176px;background:var(--brand)}
  .front__details{position:absolute;left:292px;top:100px;right:20px}
  .front__name{font-weight:700;font-size:25px;color:var(--brand)}
  .front__role{font-size:14px;color:var(--ink);margin-top:2px}
  .front__contacts{list-style:none;margin-top:14px}
  .front__contacts li{display:flex;align-items:center;gap:8px;font-size:14px;color:var(--ink);line-height:1.55;white-space:nowrap}
  .front__contacts svg{width:12px;height:12px;flex:none;fill:var(--brand)}
  .front__address{position:absolute;left:40px;bottom:48px;font-size:16px;color:var(--brand);white-space:nowrap}
  .front__rule-bottom{position:absolute;left:40px;bottom:24px;width:220px;height:1.5px;background:var(--brand)}
  /* Back */
  .card--back{top:484px;font-family:"Saira Semi Condensed",sans-serif;color:var(--on-epoxy)}
  .back__surface{position:absolute;inset:0;background:
      radial-gradient(ellipse at 30% 30%,rgba(255,255,255,.22),transparent 55%),
      radial-gradient(ellipse at 75% 80%,rgba(255,255,255,.14),transparent 50%),
      linear-gradient(135deg,var(--epoxy-mid),var(--epoxy-deep) 60%,var(--epoxy-mid))}
  .back__grinder{position:absolute;left:240px;top:34px;width:90px;height:56px;background:rgba(255,255,255,.85);border-radius:4px}
  .back__logo{position:absolute;left:220px;top:98px;display:flex;align-items:center;gap:10px}
  .back__logo-mark{width:18px;height:18px;background:var(--on-epoxy)}
  .back__logo-name{font-weight:700;font-size:26px;letter-spacing:1px;white-space:nowrap}
  .back__services{position:absolute;right:34px;top:148px;list-style:none;text-align:right}
  .back__services li{font-weight:600;font-size:13.5px;letter-spacing:.6px;text-transform:uppercase;line-height:1.35;white-space:nowrap}
  .back__services li::after{content:"";display:inline-block;width:4px;height:4px;background:var(--epoxy-light);margin-left:7px;vertical-align:middle}
</style>
</head>
<body>
<div class="canvas">

  <section class="card card--front">
    <div class="front__rule-top"></div>
    <div class="front__logo">
      <span class="front__logo-mark"></span>
      <span class="front__logo-name">Harborline Coatings</span>
    </div>
    <div class="front__divider"></div>
    <div class="front__details">
      <p class="front__name">Dane Morrow</p>
      <p class="front__role">owner</p>
      <ul class="front__contacts">
        <li><svg viewBox="0 0 24 24"><path d="M6.6 10.8a15 15 0 0 0 6.6 6.6l2.2-2.2c.3-.3.7-.4 1-.2 1.1.4 2.3.6 3.6.6.6 0 1 .4 1 1V20c0 .6-.4 1-1 1A17 17 0 0 1 3 4c0-.6.4-1 1-1h3.5c.6 0 1 .4 1 1 0 1.3.2 2.5.6 3.6.1.3 0 .7-.2 1z"/></svg>561-482-7160</li>
        <li><svg viewBox="0 0 24 24"><path d="M2 5h20v14H2zM3.5 6.5 12 13l8.5-6.5" fill="none" stroke="#2f5f95" stroke-width="2.2"/></svg>HarborlineCoatingsLLC@mailbox.example</li>
        <li><svg viewBox="0 0 24 24"><circle cx="12" cy="12" r="9" fill="none" stroke="#2f5f95" stroke-width="2"/><path d="M3 12h18M12 3c3 3 3 15 0 18M12 3c-3 3-3 15 0 18" fill="none" stroke="#2f5f95" stroke-width="1.6"/></svg>www.Harborline-CoatingsLLC.example</li>
      </ul>
    </div>
    <p class="front__address">P.O Box 8241 Lake Worth, FL 33467</p>
    <div class="front__rule-bottom"></div>
  </section>

  <section class="card card--back">
    <div class="back__surface" role="img" aria-label="Blue metallic epoxy floor texture"></div>
    <div class="back__grinder" role="img" aria-label="Icon of a worker pushing a concrete grinder"></div>
    <div class="back__logo">
      <span class="back__logo-mark"></span>
      <span class="back__logo-name">Harborline Coatings</span>
    </div>
    <ul class="back__services">
      <li>Garage Epoxy Flooring</li>
      <li>Residential Epoxy Flooring</li>
      <li>Concrete Floor Crack Repairs</li>
      <li>Concrete Floor Grinding</li>
      <li>Commercial &amp; Warehouse Epoxy Flooring</li>
      <li>Restaurant Epoxy Flooring</li>
      <li>Epoxy Countertops</li>
      <li>Non Slip Epoxy Pool Decks</li>
      <li>Textured Finishes, Flakes, Granite Coat, Metallic &amp; Quartz</li>
      <li>Free Estimates • Licensed &amp; Insured</li>
    </ul>
  </section>

</div>
</body>
</html>
```